political election

Elect Mateo Quiroga

for

Brenwick School Board Pl. ?

colors used are red, white, and blue

any other graphics are more than welcome.

need this in fine print at bottom

advertising paid for by candidate

voters of the school district

School

• red white and blue and in fine print advertisement paid for by candidate.
• graphics, art

```html
<!DOCTYPE html>
<html lang="en">
<head>
<meta charset="utf-8">
<title>Elect Mateo Quiroga – Brenwick School Board</title>
<link rel="stylesheet" href="https://fonts.googleapis.com/css2?family=Arimo:wght@400;700&display=swap">
<style>
  :root {
    --page-bg: #ece8e3;
    --paper: #ffffff;
    --sky-deep: #1f6fc0;
    --sky-mid: #3c8fd6;
    --sky-light: #d9ecfa;
    --ribbon-blue: #243f8f;
    --ribbon-shadow: #14245a;
    --candidate-red: #d4202c;
    --office-blue: #243f8f;
    --ink: #111111;
    --swoosh-dark: #3a3a3a;
    --box-yellow: #fbd22c;
    --box-orange: #f08a2a;
  }
  * { margin: 0; padding: 0; box-sizing: border-box; }
  html, body { width: 1200px; height: 1000px; overflow: hidden; }
  body {
    background: var(--page-bg);
    font-family: "Arimo", Arial, sans-serif;
    position: relative;
  }
  .poster {
    position: absolute;
    left: 275px;
    top: 70px;
    width: 650px;
    height: 860px;
    background: var(--paper);
    box-shadow: 0 10px 30px rgba(0,0,0,.25);
    overflow: hidden;
  }
  .poster__sky {
    position: absolute;
    left: 0; top: 0;
    width: 650px; height: 500px;
  }
  .poster__artwork {
    position: absolute;
    left: 190px; top: 150px;
    width: 250px; height: 290px;
    border-radius: 14px;
    background: linear-gradient(160deg, var(--box-yellow), var(--box-orange));
  }
  .ballot-ribbon {
    position: absolute;
    left: 150px; top: 490px;
    width: 350px; height: 90px;
  }
  .ballot-ribbon__label {
    position: absolute;
    left: 0; top: 508px;
    width: 650px;
    text-align: center;
    color: #fff;
    font-weight: 700;
    font-size: 30px;
  }
  .candidate-name {
    position: absolute;
    left: 0; top: 580px;
    width: 650px;
    text-align: center;
    color: var(--candidate-red);
    font-weight: 700;
    font-size: 76px;
    letter-spacing: 1px;
    line-height: 1;
  }
  .connector {
    position: absolute;
    left: 0; top: 672px;
    width: 650px;
    text-align: center;
    color: var(--ink);
    font-weight: 700;
    font-size: 30px;
  }
  .office {
    position: absolute;
    left: 0; top: 715px;
    width: 650px;
    text-align: center;
    color: var(--office-blue);
    font-weight: 700;
    font-size: 46px;
    line-height: 1.12;
  }
  .fine-print {
    position: absolute;
    left: 30px; bottom: 22px;
    font-size: 12px;
    color: var(--ink);
  }
</style>
</head>
<body>
  <main class="poster">
    <svg class="poster__sky" viewBox="0 0 650 500" aria-hidden="true">
      <defs>
        <radialGradient id="skyGlow" cx="0.48" cy="0.95" r="0.95">
          <stop offset="0" stop-color="var(--sky-light)"/>
          <stop offset="0.35" stop-color="var(--sky-mid)"/>
          <stop offset="1" stop-color="var(--sky-deep)"/>
        </radialGradient>
        <linearGradient id="swooshLeft" x1="0" x2="1">
          <stop offset="0" stop-color="var(--swoosh-dark)"/>
          <stop offset="1" stop-color="#ffffff"/>
        </linearGradient>
        <linearGradient id="swooshRight" x1="0" x2="1">
          <stop offset="0" stop-color="#ffffff"/>
          <stop offset="1" stop-color="var(--swoosh-dark)"/>
        </linearGradient>
      </defs>
      <path d="M0 0 H650 V190 Q430 300 320 450 Q160 430 0 420 Z" fill="url(#skyGlow)"/>
      <path d="M0 430 Q160 440 300 468 L300 478 Q160 455 0 446 Z" fill="url(#swooshLeft)"/>
      <path d="M335 462 Q440 320 650 210 L650 228 Q450 335 345 468 Z" fill="url(#swooshRight)"/>
    </svg>

    <div class="poster__artwork" role="img" aria-label="Illustration of a yellow ballot box with a green ballot being cast"></div>

    <svg class="ballot-ribbon" viewBox="0 0 350 90" aria-hidden="true">
      <polygon points="0,40 40,40 40,78 0,78 14,59" fill="var(--ribbon-blue)"/>
      <polygon points="310,40 350,40 336,59 350,78 310,78" fill="var(--ribbon-blue)"/>
      <polygon points="40,70 60,78 40,78" fill="var(--ribbon-shadow)"/>
      <polygon points="310,70 290,78 310,78" fill="var(--ribbon-shadow)"/>
      <rect x="40" y="14" width="270" height="56" fill="var(--ribbon-blue)"/>
    </svg>
    <p class="ballot-ribbon__label">Elect</p>

    <h1 class="candidate-name">Mateo Quiroga</h1>
    <p class="connector">for</p>
    <h2 class="office">Brenwick School<br>Board Pl.</h2>
    <p class="fine-print">advertising paid for by candidate</p>
  </main>
</body>
</html>
```